Velmar Industrial Coatings

We are looking to improve our business cards. Our company installs industrial floor and wall coatings in industrial, chemical and food processing plants.
Our coatings which consist of epoxy, urethane, and vinyl esters provide chemical and abrasion resistant surface with non-skid properties that are easy to clean.

Target Market(s)

food manufacturing, chemical plants, breweries and wineries, warehouses, clean room floors.

Industry/Entity Type

Construction

Contact Information for Business Card

improved current logo.

Colors

Designer to choose colors to be used in the design.

Requirements
Must have
• the information from uploaded file
Nice to have
• "Built to last on every floor you own."

```html
<!DOCTYPE html>
<html lang="en">
<head>
<meta charset="UTF-8">
<title>Velmar Industrial Coatings – Business Card</title>
<link href="https://fonts.googleapis.com/css2?family=Montserrat:wght@500;800&family=Roboto:wght@400;500&display=swap" rel="stylesheet">
<style>
  :root{
    --page:#2a2a2c;
    --card-light:#f1f1f1;
    --card-dark:#1e1c1d;
    --navy:#1a2266;
    --blue:#1f4fa6;
    --sky:#1d7cc8;
    --ink:#4a4a4c;
    --muted:#8a8a8c;
    --step-1:#2c2c30;
    --step-2:#38393d;
    --white:#ffffff;
    --url-light:#d8d8d8;
  }
  *{margin:0;padding:0;box-sizing:border-box}
  html,body{width:1200px;height:900px;overflow:hidden;background:var(--page)}
  .canvas{width:1200px;height:900px;display:flex;flex-direction:column;align-items:center;justify-content:center;gap:40px}
  .card{position:relative;width:700px;height:400px;overflow:hidden;box-shadow:0 10px 30px rgba(0,0,0,.45)}

  /* brand block */
  .brand{position:absolute;display:flex;align-items:flex-start;gap:16px}
  .brand__square{width:54px;height:54px;flex:none}
  .brand__name{font-family:"Montserrat",sans-serif;font-weight:800;font-size:24px;line-height:1.02;text-transform:uppercase;letter-spacing:.5px}
  .brand__tagline{font-family:"Montserrat",sans-serif;font-weight:500;font-size:10px;letter-spacing:.6px;text-transform:uppercase;margin-top:5px}

  /* front */
  .card--front{background:var(--card-light)}
  .card--front .brand{left:170px;top:52px}
  .card--front .brand__square{background:var(--navy)}
  .card--front .brand__name{color:var(--navy)}
  .card--front .brand__tagline{color:var(--muted)}

  .contact{position:absolute;left:60px;top:170px;list-style:none;font-family:"Roboto",sans-serif;font-size:15px;color:var(--ink);line-height:22px}
  .contact li{display:flex;align-items:center;gap:10px}
  .contact svg{width:13px;height:13px;fill:var(--blue);flex:none}

  .person{position:absolute;right:60px;top:188px;text-align:right;font-family:"Roboto",sans-serif}
  .person__name{font-weight:500;font-size:22px;line-height:28px;color:var(--blue);text-transform:uppercase;letter-spacing:.5px}
  .person__role{font-size:15px;line-height:20px;color:var(--ink)}
  .address{position:absolute;right:60px;top:256px;text-align:right;font-family:"Roboto",sans-serif;font-style:normal;font-size:15px;color:var(--ink);line-height:21px}

  .band{position:absolute;left:0;right:0;bottom:22px;height:48px;background:linear-gradient(90deg,var(--blue) 0%,var(--blue) 55%,var(--navy) 78%,var(--sky) 80%,var(--sky) 100%);display:flex;align-items:center;padding-left:42px}
  .band__url{font-family:"Roboto",sans-serif;font-weight:500;font-size:15px;color:var(--white);letter-spacing:.3px}
  .band__square{position:absolute;left:548px;top:6px;width:36px;height:36px;background:var(--navy);border:2px solid var(--white)}

  /* back */
  .card--back{background:var(--card-dark)}
  .steps{position:absolute;right:0;top:0;width:320px;height:400px}
  .card--back .brand{left:70px;top:120px}
  .card--back .brand__square{background:var(--sky)}
  .card--back .brand__name{color:var(--white)}
  .card--back .brand__tagline{color:var(--white)}
  .back__url{position:absolute;left:140px;top:270px;font-family:"Roboto",sans-serif;font-size:16px;color:var(--url-light);letter-spacing:2px}
</style>
</head>
<body>
<main class="canvas">

  <section class="card card--front" aria-label="Business card front">
    <div class="brand">
      <span class="brand__square"></span>
      <div>
        <p class="brand__name">Velmar Industrial<br>Coatings</p>
        <p class="brand__tagline">Built to last on every floor you own</p>
      </div>
    </div>

    <ul class="contact">
      <li><svg viewBox="0 0 24 24"><path d="M6.6 10.8a15.1 15.1 0 0 0 6.6 6.6l2.2-2.2a1 1 0 0 1 1-.25 11.4 11.4 0 0 0 3.6.6 1 1 0 0 1 1 1V20a1 1 0 0 1-1 1A17 17 0 0 1 3 4a1 1 0 0 1 1-1h3.5a1 1 0 0 1 1 1c0 1.25.2 2.45.6 3.6a1 1 0 0 1-.25 1z"/></svg>(800) 555-0142</li>
      <li><svg viewBox="0 0 24 24"><path d="M6.6 10.8a15.1 15.1 0 0 0 6.6 6.6l2.2-2.2a1 1 0 0 1 1-.25 11.4 11.4 0 0 0 3.6.6 1 1 0 0 1 1 1V20a1 1 0 0 1-1 1A17 17 0 0 1 3 4a1 1 0 0 1 1-1h3.5a1 1 0 0 1 1 1c0 1.25.2 2.45.6 3.6a1 1 0 0 1-.25 1z"/></svg>(360) 555-0187</li>
      <li><svg viewBox="0 0 24 24"><path d="M6 3h12v5H6zM4 9h16a2 2 0 0 1 2 2v6h-4v4H6v-4H2v-6a2 2 0 0 1 2-2zm4 7v3h8v-3z"/></svg>(360) 555-0189</li>
      <li><svg viewBox="0 0 24 24"><path d="M7 1h10a2 2 0 0 1 2 2v18a2 2 0 0 1-2 2H7a2 2 0 0 1-2-2V3a2 2 0 0 1 2-2zm0 3v14h10V4z"/></svg>(360) 555-0163</li>
      <li><svg viewBox="0 0 24 24"><path d="M2 5h20v14H2zm2 2v.5l8 5 8-5V7z"/></svg>reid@velmarfloors.com</li>
    </ul>

    <div class="person">
      <p class="person__name">Reid Calloway</p>
      <p class="person__role">Managing Director</p>
    </div>
    <address class="address">
      Velmar Group LLC<br>PO Box 214, Alder Creek, WA 98520
    </address>

    <div class="band">
      <span class="band__url">www.velmarfloors.com</span>
      <span class="band__square"></span>
    </div>
  </section>

  <section class="card card--back" aria-label="Business card back">
    <svg class="steps" viewBox="0 0 320 400" aria-hidden="true">
      <rect x="60" y="0" width="260" height="400" fill="var(--step-1)"/>
      <rect x="110" y="0" width="210" height="150" fill="var(--step-2)"/>
      <rect x="200" y="150" width="120" height="250" fill="var(--step-2)" opacity=".6"/>
    </svg>
    <div class="brand">
      <span class="brand__square"></span>
      <div>
        <p class="brand__name">Velmar Industrial<br>Coatings</p>
        <p class="brand__tagline">Built to last on every floor you own</p>
      </div>
    </div>
    <p class="back__url">www.velmarfloors.com</p>
  </section>

</main>
</body>
</html>
```